依頼詳細
基本的な掲載コンテンツは変更はありません。現在のデザインは文字だけが目立つ為、今回は、都会的な感じでお願いしたいと言う抽象的な表現です。
作成頂いたラフ案をベースに他のページも制作したいと考えているため、その点も考慮して下さい。また、サイトはビジネスブログを利用して制作致します。
画像などは添付ファイルのものを利用して下さい。そしてデザインに合った他の素材を使って下さい。(素材は基本的にはご準備下さい。良い素材ならば有料素材を使っても構いませんが、その際は、素材にかかる費用をお知らせください。)
サイトの幅は、Zorbiと同じ幅でお願いします。(背景は別)
電話番号は大きくお願いします。
サイトURL
http://www.mokuren-hiroba.com/
ページ数
1ページ
希望イメージ
シンプル 複雑
単色 カラフル
暗い 明るい
日常 高級
遊び心 厳粛
未来的 伝統的
女性的 男性的
希望する色
特に指定はございません。求人広告会社に相応しい色合いでお願いします。
納品ファイル
• 高解像度JPG (.jpg)
• フォトショップ形式 (.psd)
補足説明
イメージに近いサイト http://www.sora-teppan.jp/
参考ページ http://www.sora-teppan.jp/kansai/ov/
デザインによりボタン名称など変更しても構いません。場合によってはページ内容も変更致します。ご提案があれば、歓迎です。
追加の情報です。
色合い、配置など含めて出来ましたら現在のサイトとは、まったく違った感じが欲しいのです。
現在のサイトは意識せずにご提案をお願い致します。
■ 選んだ理由

最終的な決定権は当社のクライアントですが、総合的なデザインの良さとわかり易さ、それと求人広告会社らしいサイトに見えるという事で決定致しました。
特に、広告の上に虫めがねがあるのが、決め手となりました。
有難うございました。

■ 提案者全員のお礼・コメント

皆さま方のご提案はどれも捨てがたく、デザイン的にも内容的にも大変良かったと思います。
せっかくご提案頂きましたが、決定とならず大変申し訳ありませんでした。
これに懲りず今後も案件がございましたら宜しくお願い致します。
有難うございました。

```html
<!DOCTYPE html>
<html lang="ja">
<head>
<meta charset="utf-8">
<title>株式会社もくれんワークス</title>
<link href="https://fonts.googleapis.com/css2?family=Noto+Sans+JP:wght@400;700;900&display=swap" rel="stylesheet">
<style>
:root{
  --blue:#1f6fd1;
  --blue-dark:#0d4fa8;
  --blue-light:#5aa0ea;
  --bg:#e9eef5;
  --text:#444;
  --muted:#888;
  --line:#d7dfea;
  --white:#fff;
}
*{margin:0;padding:0;box-sizing:border-box}
html,body{width:793px;height:1200px;overflow:hidden}
body{background:var(--bg);font-family:"Noto Sans JP",sans-serif;color:var(--text);font-size:10px}
.page{width:793px;height:1200px;position:relative}
.util{height:22px;background:var(--white);display:flex;gap:14px;padding:6px 60px;font-size:8px;color:#555}
.util span::before{content:"";display:inline-block;width:7px;height:7px;background:var(--blue);margin-right:3px;vertical-align:-1px}
.header{height:76px;background:var(--white);display:flex;align-items:center;justify-content:space-between;padding:0 55px}
.brand{display:flex;align-items:center;gap:8px}
.brand-mark{width:14px;height:14px;background:var(--blue-dark)}
.brand-name{color:var(--blue-dark);font-weight:700;font-size:20px;line-height:1;white-space:nowrap}
.contact{display:flex;align-items:center;gap:8px}
.tel{display:flex;align-items:center;gap:6px}
.tel-label{font-size:7px;color:var(--muted);display:block}
.tel-num{font-size:22px;font-weight:900;color:var(--blue-dark);letter-spacing:1px;line-height:1.1}
.mail-btn{background:var(--blue);color:var(--white);font-size:9px;font-weight:700;padding:6px 10px;border-radius:3px;white-space:nowrap}
.nav{height:28px;background:linear-gradient(var(--blue-light),var(--blue-dark));display:flex;justify-content:center}
.nav a{width:134px;text-align:center;color:var(--white);font-weight:700;font-size:11px;line-height:28px;text-decoration:none;border-right:1px solid rgba(255,255,255,.3)}
.nav a.active{background:var(--white);color:var(--blue-dark)}
.hero{height:296px;margin:5px auto 0;width:793px;position:relative;background:linear-gradient(100deg,#dde6ef,#f6f8fb 45%,#d9e2ec)}
.hero-copy{position:absolute;left:170px;top:95px;font-size:20px;font-weight:900;color:var(--blue-dark);line-height:1.6;white-space:nowrap}
.box{width:686px;margin:0 auto;background:var(--white);border:1px solid var(--line)}
.box h2{height:22px;background:linear-gradient(var(--blue-light),var(--blue));color:var(--white);font-size:10px;padding-left:12px;line-height:22px}
.message{margin-top:26px;height:210px}
.message p{padding:14px 22px 0;font-size:8.5px;line-height:1.9;color:#666}
.news{margin-top:48px}
.news li{list-style:none;display:flex;gap:24px;font-size:8.5px;padding:7px 22px;border-bottom:1px dotted var(--line)}
.news li b{font-weight:400;color:#666}
.news li span{color:var(--blue)}
.more{background:var(--line);text-align:center;font-size:8px;padding:5px;color:#555}
.pagetop{position:absolute;right:60px;top:992px;font-size:8px;color:#555}
.footer{position:absolute;left:0;bottom:0;width:793px;height:182px;background:var(--blue);color:var(--white);text-align:center}
.footer .links{display:flex;justify-content:center;gap:16px;font-size:8px;padding:14px 0 26px}
.footer .links span::before{content:"";display:inline-block;width:6px;height:6px;background:var(--white);margin-right:3px}
.foot-info{display:flex;justify-content:center;gap:16px;align-items:center}
.foot-brand{display:flex;align-items:center;gap:6px}
.foot-brand .brand-mark{width:11px;height:11px;background:var(--white)}
.foot-brand .brand-name{color:var(--white);font-size:16px}
.foot-addr{text-align:left;font-size:8px;line-height:1.7}
.foot-addr b{font-size:11px}
.copy{font-size:7px;margin-top:20px;opacity:.85}
</style>
</head>
<body>
<div class="page">
  <div class="util"><span>HOME</span><span>求人情報</span><span>会社案内</span><span>営業案内</span><span>エリアマップ</span><span>お問合せ</span><span>リンク</span><span>プライバシーポリシー</span></div>
  <header class="header">
    <div class="brand"><span class="brand-mark"></span><span class="brand-name">MOKUREN WORKS</span></div>
    <div class="contact">
      <div class="tel">
        <svg width="22" height="22" viewBox="0 0 24 24"><circle cx="12" cy="12" r="12" fill="#0d4fa8"/><path d="M8 6l2 0 1 3-1.5 1a7 7 0 0 0 4 4l1-1.5 3 1 0 2c-5 1-10-4-9-9.5z" fill="#fff"/></svg>
        <div><span class="tel-label">お気軽にお問い合わせください</span><span class="tel-num">077-000-4182</span></div>
      </div>
      <div class="mail-btn">✉ お問い合わせはコチラ</div>
    </div>
  </header>
  <nav class="nav"><a>HOME</a><a>求人情報</a><a>会社案内</a><a class="active">営業案内</a><a>サンプル</a></nav>
  <div class="hero" role="img" aria-label="働く人々と求人情報誌の写真コラージュ">
    <div class="hero-copy">滋賀県での求人広告は、地域に密着した<br>求人情報誌「MOKUREN WORKS」の株式会社もくれんワークス</div>
  </div>
  <section class="box message">
    <h2>MESSAGE</h2>
    <p>「株式会社もくれんワークス」は、地域密着の求人情報誌を発行する専門会社です。<br>
    地元の企業さまと働きたい方をつなぐため、毎週新しい求人情報をお届けしています。<br>
    求人広告のご相談から原稿作成まで、経験豊富なスタッフが丁寧にサポートいたします。<br>
    「良い人材に出会いたい」というお声に応えるため、掲載後のフォローも大切にしています。<br>
    これからも地域の皆さまに愛される情報誌を目指してまいります。</p>
  </section>
  <section class="box news">
    <h2>NEWS</h2>
    <ul>
      <li><b>2013/03/25</b><span>最新号を発行しました</span></li>
      <li><b>2013/03/18</b><span>ゴールデンウィーク休業のお知らせ</span></li>
      <li><b>2013/03/11</b><span>掲載エリアを拡大しました</span></li>
      <li><b>2013/03/04</b><span>最新号を発行しました</span></li>
      <li><b>2013/02/25</b><span>ホームページを開設しました</span></li>
      <li><b>2013/02/18</b><span>最新号を発行しました</span></li>
    </ul>
    <div class="more">▼ 過去の記事を見る</div>
  </section>
  <div class="pagetop">▲ PAGE TOP</div>
  <footer class="footer">
    <div class="links"><span>HOME</span><span>求人情報</span><span>会社案内</span><span>営業案内</span><span>エリアマップ</span><span>お問合せ</span><span>リンク</span><span>プライバシーポリシー</span></div>
    <div class="foot-info">
      <div class="foot-brand"><span class="brand-mark"></span><span class="brand-name">MOKUREN WORKS</span></div>
      <div class="foot-addr">〒520-0000 滋賀県さくら町1-2-3<br><b>☎ 077-000-4182</b></div>
    </div>
    <div class="copy">Copyright (C) MOKUREN WORKS, All Rights Reserved.</div>
  </footer>
</div>
</body>
</html>
```